VerdaTurfix - 11" x 4" Door Hanger, full color both sides

We need a door hanger designed, 11" x 4", full color both sides, We are a lawn care company that provides lawn mowing, and other services to clients. This door hanger will be place on the 9 neighbors of our current clients. The ad needs to state that we provided lawn service to one of their neighbors today, and that we are in their neighborhood each week on that day. The door hanger will have 4 printings, substituting the day of Tuesday, Wednesday, Thursday, and Friday. All the art work and text will remain the same except the day of the week. For information about VerdaTurfix, please visit our website www.verdaturfix.net. The main emphasis of the message should be that we are their every week on that day, and the benefits to them of using our service (ie. quality time with their family, golf, sports, resting, etc., instead of mowing the lawn). At the bottom of the door hanger will be a coupon offering their tenth (10th) lawn service free, which is the same as a 10% discount.

I have uploaded a template files for the front and back of an 11 x 4 door hanger, The templates are pdf, jpeg, or eps files. The final product can be a pdf, jpeg, or eps file.

Target Market(s)

Neighbors of our existing clients

Industry/Entity Type

Lawn Care

Font styles to use
Serif

Requirements
Must have
• Professional design and art, Short conversational message that relays the following thoughts:
• 1. We mowed your neighbor's lawn today!
• 2. We are in your neighborhood every Tuesday!
• 3. Our lawn service is guaranteed.
• 4. Call to action - Call us today! 555-014-7382
• 5. Of course our contact info, name, phone number, website address.
• 6. Coupon at bottom for "10th lawn service Free!"
Nice to have
• Art work from our website is fine to use, That carries our theme throughout our campaign.
Should not have
• Very wordy. This is basically a billboard, Have very few seconds to grab their attention.

```html
<!DOCTYPE html>
<html lang="en">
<head>
<meta charset="utf-8">
<title>VerdaTurfix Door Hangers</title>
<link rel="stylesheet" href="https://fonts.googleapis.com/css2?family=Open+Sans:ital,wght@0,400;0,600;1,400&family=Roboto+Condensed:wght@700&display=swap">
<style>
  :root {
    --page: #ecebe7;
    --green-deep: #0f4a24;
    --green-mid: #17702f;
    --green-bright: #3faa2c;
    --green-lime: #7ccd2a;
    --green-check: #8fd33a;
    --yellow: #e6ec2a;
    --white: #ffffff;
    --footer: #f3f4f1;
  }
  * { box-sizing: border-box; margin: 0; padding: 0; }
  html, body { width: 1200px; height: 1104px; overflow: hidden; background: var(--page); }
  .canvas { position: relative; width: 1200px; height: 1104px; }

  .hanger {
    position: absolute; top: 106px; width: 336px; height: 922px;
    border-radius: 16px 16px 12px 12px; overflow: hidden;
    background: var(--green-deep);
    box-shadow: 0 4px 10px rgba(0,0,0,.18);
    font-family: "Open Sans", sans-serif; color: var(--white);
  }
  .hanger--front { left: 166px; }
  .hanger--back { left: 662px; }
  .hanger__art { position: absolute; inset: 0; }

  .headline {
    position: absolute; top: 24px; left: 0; width: 100%;
    text-align: center; font-family: "Roboto Condensed", sans-serif;
    font-weight: 700; font-size: 22px; line-height: 29px; text-transform: uppercase;
    white-space: nowrap;
  }

  .brand {
    position: absolute; top: 508px; left: 0; width: 100%; text-align: center;
    font-weight: 600; font-size: 40px; letter-spacing: 1px; color: #eef0ec;
    white-space: nowrap;
  }

  .tagline {
    position: absolute; top: 562px; left: 0; width: 100%; text-align: center;
    font-style: italic; font-size: 19px; line-height: 27px; color: var(--yellow);
  }
  .guarantee {
    position: absolute; top: 625px; left: 0; width: 100%; text-align: center;
    font-size: 14px; white-space: nowrap;
  }

  .services { position: absolute; top: 574px; left: 10px; list-style: none; }
  .services li {
    display: flex; align-items: center; gap: 7px; white-space: nowrap;
    font-size: 16px; line-height: 24px; color: var(--green-check);
  }
  .services svg { width: 13px; height: 11px; flex: none; }

  .coupon {
    position: absolute; left: 10px; width: 316px; height: 110px;
    border: 2px solid var(--green-lime); border-radius: 8px; overflow: hidden;
    background:
      linear-gradient(180deg, rgba(255,255,255,0) 55%, rgba(20,80,20,.55) 100%),
      linear-gradient(180deg, #9bcf6a 0%, #55a32f 45%, #2f7a1f 100%);
    font-family: "Roboto Condensed", sans-serif; font-weight: 700;
    white-space: nowrap;
  }
  .hanger--front .coupon { top: 670px; }
  .hanger--back .coupon { top: 710px; }
  .coupon__label { position: absolute; top: 16px; left: 150px; font-size: 20px; letter-spacing: -0.5px; line-height: 1; }
  .coupon__big { position: absolute; top: 10px; left: 20px; font-size: 82px; line-height: 1; letter-spacing: -2px; }
  .coupon__rest { position: absolute; top: 42px; left: 96px; font-size: 54px; line-height: 1; }
  .coupon__rest small { font-size: 40px; }
  .coupon__ribbon {
    position: absolute; top: 12px; right: -34px; width: 116px; height: 18px;
    transform: rotate(45deg); background: var(--green-lime);
    font-family: "Open Sans", sans-serif; font-weight: 600; font-size: 10px;
    line-height: 18px; text-align: center; letter-spacing: .5px;
  }

  .cta { font-family: "Roboto Condensed", sans-serif; font-weight: 700; white-space: nowrap; }
  .cta__label { color: var(--yellow); }
  .cta--stacked .cta__label { position: absolute; top: 794px; left: 0; width: 100%; text-align: center; font-size: 25px; letter-spacing: -0.5px; }
  .cta--stacked .cta__phone { position: absolute; top: 822px; left: 0; width: 100%; text-align: center; font-size: 48px; letter-spacing: 1px; }
  .cta--inline { position: absolute; top: 842px; left: 14px; width: 310px; display: flex; align-items: baseline; justify-content: space-between; }
  .cta--inline .cta__label { font-size: 18px; letter-spacing: -0.5px; flex: none; }
  .cta--inline .cta__phone { font-size: 33px; letter-spacing: 0.5px; flex: none; }

  .footer {
    position: absolute; bottom: 0; left: 0; width: 100%; height: 30px;
    background: var(--footer); text-align: center;
    font-weight: 600; font-size: 18px; line-height: 30px; color: var(--green-deep);
  }
</style>
</head>
<body>
<main class="canvas">

  <article class="hanger hanger--front">
    <svg class="hanger__art" viewBox="0 0 336 922" width="336" height="922">
      <defs>
        <linearGradient id="topFront" x1="0" y1="0" x2="0" y2="1">
          <stop offset="0" stop-color="#127a32"/>
          <stop offset="1" stop-color="#1f9a35"/>
        </linearGradient>
        <linearGradient id="yardFront" x1="0" y1="0" x2="0" y2="1">
          <stop offset="0" stop-color="#4c5a4a"/>
          <stop offset=".45" stop-color="#7a4a50"/>
          <stop offset=".6" stop-color="#67b040"/>
          <stop offset="1" stop-color="#4f9e30"/>
        </linearGradient>
        <radialGradient id="gardenFront" cx=".5" cy=".5" r=".6">
          <stop offset="0" stop-color="#c05a8a"/>
          <stop offset=".5" stop-color="#6a9a45"/>
          <stop offset="1" stop-color="#5fa63a"/>
        </radialGradient>
      </defs>
      <rect width="336" height="490" fill="url(#topFront)"/>
      <path d="M0,222 C40,130 150,90 336,96 L336,112 C150,110 40,150 0,240 Z" fill="var(--green-lime)"/>
      <path role="img" aria-label="Photo of a house front door with shrubs and a green lawn"
            d="M0,240 C40,150 150,110 336,112 L336,486 L0,486 Z" fill="url(#yardFront)"/>
      <rect y="484" width="336" height="4" fill="var(--green-bright)"/>
      <circle cx="242" cy="403" r="94" fill="var(--green-deep)"/>
      <circle role="img" aria-label="Photo of a garden with flowers in front of a porch" cx="242" cy="403" r="86" fill="url(#gardenFront)" stroke="#e8efe4" stroke-width="4"/>
      <circle cx="168" cy="139" r="56" fill="var(--page)" stroke="var(--green-mid)" stroke-width="3"/>
    </svg>

    <h1 class="headline">We mowed your neighbor's<br>lawn today!</h1>
    <p class="brand">VERDATURFIX</p>
    <p class="tagline">We are in your<br>neighborhood every Tuesday!</p>
    <p class="guarantee">Our lawn service is guaranteed.</p>

    <div class="coupon">
      <span class="coupon__label">LAWN SERVICE</span>
      <span class="coupon__big">10</span>
      <span class="coupon__rest"><small>TH</small> FREE!</span>
      <span class="coupon__ribbon">DISCOUNT</span>
    </div>

    <div class="cta cta--stacked">
      <p class="cta__label">CALL US TODAY!</p>
      <p class="cta__phone">555-014-7382</p>
    </div>
    <p class="footer">www.verdaturfix.net</p>
  </article>

  <article class="hanger hanger--back">
    <svg class="hanger__art" viewBox="0 0 336 922" width="336" height="922">
      <defs>
        <linearGradient id="topBack" x1="0" y1="0" x2="0" y2="1">
          <stop offset="0" stop-color="#127a32"/>
          <stop offset="1" stop-color="#1f9a35"/>
        </linearGradient>
        <linearGradient id="yardBack" x1="0" y1="0" x2="0" y2="1">
          <stop offset="0" stop-color="#1f3a1e"/>
          <stop offset=".55" stop-color="#2f5a28"/>
          <stop offset=".75" stop-color="#5aa83a"/>
          <stop offset="1" stop-color="#4e9a30"/>
        </linearGradient>
        <radialGradient id="grassBack" cx=".5" cy=".5" r=".6">
          <stop offset="0" stop-color="#6fb845"/>
          <stop offset="1" stop-color="#3e8a28"/>
        </radialGradient>
      </defs>
      <rect width="336" height="490" fill="url(#topBack)"/>
      <path d="M0,222 C40,130 150,90 336,96 L336,112 C150,110 40,150 0,240 Z" fill="var(--green-lime)"/>
      <path role="img" aria-label="Photo of a family playing with balloons on a garden lawn"
            d="M0,240 C40,150 150,110 336,112 L336,486 L0,486 Z" fill="url(#yardBack)"/>
      <rect y="484" width="336" height="4" fill="var(--green-bright)"/>
      <circle cx="256" cy="420" r="94" fill="var(--green-deep)"/>
      <circle role="img" aria-label="Photo of a hand resting on thick green grass" cx="256" cy="420" r="86" fill="url(#grassBack)" stroke="#e8efe4" stroke-width="4"/>
      <line x1="0" y1="139" x2="114" y2="139" stroke="#0b3a1c" stroke-width="1"/>
      <circle cx="168" cy="139" r="56" fill="var(--page)" stroke="var(--green-mid)" stroke-width="3"/>
    </svg>

    <h2 class="headline">We mowed your neighbor's<br>lawn today!</h2>
    <p class="brand">VERDATURFIX</p>

    <ul class="services">
      <li><svg viewBox="0 0 13 11"><path d="M1 6 L5 10 L12 1" fill="none" stroke="var(--green-check)" stroke-width="2"/></svg>Weekly or bi-weekly lawn mowing</li>
      <li><svg viewBox="0 0 13 11"><path d="M1 6 L5 10 L12 1" fill="none" stroke="var(--green-check)" stroke-width="2"/></svg>Fertilization &amp; weed-control programs</li>
      <li><svg viewBox="0 0 13 11"><path d="M1 6 L5 10 L12 1" fill="none" stroke="var(--green-check)" stroke-width="2"/></svg>Landscape services</li>
      <li><svg viewBox="0 0 13 11"><path d="M1 6 L5 10 L12 1" fill="none" stroke="var(--green-check)" stroke-width="2"/></svg>Sprinkler repair</li>
      <li><svg viewBox="0 0 13 11"><path d="M1 6 L5 10 L12 1" fill="none" stroke="var(--green-check)" stroke-width="2"/></svg>Landscape lighting</li>
    </ul>

    <div class="coupon">
      <span class="coupon__label">LAWN SERVICE</span>
      <span class="coupon__big">10</span>
      <span class="coupon__rest"><small>TH</small> FREE!</span>
      <span class="coupon__ribbon">DISCOUNT</span>
    </div>

    <div class="cta cta--inline">
      <span class="cta__label">CALL US TODAY!</span>
      <span class="cta__phone">555-014-7382</span>
    </div>
    <p class="footer">www.verdaturfix.net</p>
  </article>

</main>
</body>
</html>
```